Bright Acorns Business Card Design

Bright Acorns - Cultivating Natural Play Spaces

Bright Acorns is a company that focuses on promoting the design, construction, consultation and support of natural, creative and organic play spaces for Early Childhood and learning environments.

We need a professional Business Card designed that is unique modern and creative. The Philosophy of the company is nostalgic so the business and will need to reflect this but also reflect that our ideas are modern and cutting edge.

The business card will need to be a talking point, by either having a unique size, quality and/or placement of logo or other quality.

I am more interested in using natural recycled paper, as this would reflect the philosophy of the company, but I open to seeing colour used creatively.
Updates

Hi Designers, Apologies, Could you please add www.brightacorns.com.au to the business card. Thanks very much.

Hi All, Thank you all for your submission thus far. Please note the fonts for used in the logo are: Ostrich Sans Black and Archer Semi Bold. If these could be considered for contact details, my name etc. Also please show the design on a recycled brown card if possible as this will be the type of card I will use when printing. Thanks so much.

Target Market(s)

Child Care Providers, Play Industry Professionals

Industry/Entity Type

Business

Contact Information for Business Card

Bright Acorns
Growing Outdoor Play Places
Marlene Okafor
0419 862 304
marlene@brightacorns.com.au

Font styles to use
Sans Serif

Requirements
Must have
• The Logo and the Details plus the below phrase
• Bright Acorns - Cultivating Natural Play Spaces
Nice to have
• A bit of colour, but not too much colour.
Should not have
• Not to have a white background, recycled brown card only

```html
<!DOCTYPE html>
<html lang="en">
<head>
<meta charset="UTF-8">
<title>Bright Acorns Business Card Design</title>
<link rel="stylesheet" href="https://fonts.googleapis.com/css2?family=Oswald:wght@500;600&family=Arvo:wght@400&display=swap">
<style>
  :root {
    --backdrop: #ebe7df;
    --kraft: #d3cab4;
    --ink-grey: #77736c;
    --ink-coral: #d8665d;
    --shadow: rgba(60, 45, 25, 0.22);
  }
  * { box-sizing: border-box; margin: 0; padding: 0; }
  html, body {
    width: 1200px;
    height: 1200px;
    overflow: hidden;
    background: var(--backdrop);
  }
  .sheet {
    width: 1200px;
    height: 1200px;
    display: flex;
    flex-direction: column;
    align-items: center;
    justify-content: center;
    gap: 60px;
  }
  .card {
    position: relative;
    width: 900px;
    height: 514px;
    background: var(--kraft);
    box-shadow: 0 6px 18px var(--shadow);
    color: var(--ink);
  }
  .card--grey { --ink: var(--ink-grey); }
  .card--coral { --ink: var(--ink-coral); }

  .brand {
    position: absolute;
    top: 150px;
    right: 90px;
    display: flex;
    flex-direction: column;
    align-items: center;
    gap: 8px;
    color: var(--ink);
  }
  .brand__row {
    display: flex;
    align-items: center;
    gap: 14px;
    white-space: nowrap;
  }
  .brand__dot {
    width: 30px;
    height: 30px;
    border-radius: 50%;
    background: var(--ink);
    flex: none;
  }
  .brand__name {
    font-family: "Oswald", sans-serif;
    font-weight: 600;
    font-size: 54px;
    letter-spacing: 1px;
    text-transform: uppercase;
    line-height: 1;
  }
  .brand__tagline {
    font-family: "Arvo", serif;
    font-size: 17px;
    text-transform: uppercase;
    letter-spacing: 0.5px;
    text-align: center;
    line-height: 1.2;
    white-space: nowrap;
  }

  .holder {
    position: absolute;
    left: 62px;
    top: 290px;
    font-family: "Oswald", sans-serif;
    font-weight: 500;
    font-size: 28px;
    letter-spacing: 1.5px;
    text-transform: uppercase;
    line-height: 1.2;
    color: var(--ink);
  }
  .contact {
    position: absolute;
    left: 62px;
    top: 356px;
    list-style: none;
    font-family: "Arvo", serif;
    font-size: 20px;
    line-height: 1.3;
    color: var(--ink);
    display: flex;
    flex-direction: column;
    gap: 6px;
  }
  .contact__item {
    display: flex;
    align-items: center;
    gap: 14px;
    white-space: nowrap;
  }
  .contact__icon {
    width: 20px;
    height: 20px;
    flex: none;
    fill: var(--ink);
  }
  .contact__icon .cut {
    fill: none;
    stroke: var(--kraft);
  }
</style>
</head>
<body>
<main class="sheet">

  <article class="card card--grey">
    <div class="brand">
      <div class="brand__row">
        <span class="brand__dot"></span>
        <span class="brand__name">Bright Acorns</span>
      </div>
      <p class="brand__tagline">Growing<br>Outdoor Play Places</p>
    </div>
    <h2 class="holder">Marlene Okafor</h2>
    <ul class="contact">
      <li class="contact__item">
        <svg class="contact__icon" viewBox="0 0 20 20"><path d="M3 7c0-2 3-4 7-4s7 2 7 4v1h-4V6.5c-1-.5-5-.5-6 0V8H3z"/><rect x="4" y="10" width="12" height="7" rx="1.5"/></svg>
        <span>0419 862 304</span>
      </li>
      <li class="contact__item">
        <svg class="contact__icon" viewBox="0 0 20 20"><rect x="2" y="4" width="16" height="12" rx="1"/><path class="cut" d="M2.5 5l7.5 6 7.5-6" stroke-width="1.6"/></svg>
        <span>marlene@brightacorns.com.au</span>
      </li>
      <li class="contact__item">
        <svg class="contact__icon" viewBox="0 0 20 20"><circle cx="10" cy="10" r="8"/><path class="cut" d="M2 10h16M10 2c-3 3-3 13 0 16M10 2c3 3 3 13 0 16" stroke-width="1.3"/></svg>
        <span>www.brightacorns.com.au</span>
      </li>
    </ul>
  </article>

  <article class="card card--coral">
    <div class="brand">
      <div class="brand__row">
        <span class="brand__dot"></span>
        <span class="brand__name">Bright Acorns</span>
      </div>
      <p class="brand__tagline">Growing<br>Outdoor Play Places</p>
    </div>
    <h2 class="holder">Marlene Okafor</h2>
    <ul class="contact">
      <li class="contact__item">
        <svg class="contact__icon" viewBox="0 0 20 20"><path d="M3 7c0-2 3-4 7-4s7 2 7 4v1h-4V6.5c-1-.5-5-.5-6 0V8H3z"/><rect x="4" y="10" width="12" height="7" rx="1.5"/></svg>
        <span>0419 862 304</span>
      </li>
      <li class="contact__item">
        <svg class="contact__icon" viewBox="0 0 20 20"><rect x="2" y="4" width="16" height="12" rx="1"/><path class="cut" d="M2.5 5l7.5 6 7.5-6" stroke-width="1.6"/></svg>
        <span>marlene@brightacorns.com.au</span>
      </li>
      <li class="contact__item">
        <svg class="contact__icon" viewBox="0 0 20 20"><circle cx="10" cy="10" r="8"/><path class="cut" d="M2 10h16M10 2c-3 3-3 13 0 16M10 2c3 3 3 13 0 16" stroke-width="1.3"/></svg>
        <span>www.brightacorns.com.au</span>
      </li>
    </ul>
  </article>

</main>
</body>
</html>
```